Lotus Leaf Kitchen Road Billboard

Road Billboard I need all of this information on it
Authentic Thai Food Bangkok Style
6.5 Miles on the right
4126 Maple Ridge Rd Otto NC
828-555-4172

```html
<!DOCTYPE html>
<html lang="en">
<head>
<meta charset="utf-8">
<title>Lotus Leaf Kitchen Road Billboard</title>
<link rel="stylesheet" href="https://fonts.googleapis.com/css2?family=Alegreya+Sans:wght@500;800&family=Montserrat:wght@500&family=Oswald:wght@500&family=Roboto+Condensed:wght@500&display=swap">
<style>
  :root {
    --page: #14161c;
    --mustard: #d9a92b;
    --ink: #111111;
    --crimson: #8e1a1a;
    --white: #ffffff;
    --ember-dark: #120807;
    --ember-mid: #6b2208;
    --ember-hot: #e07a1c;
  }
  html, body {
    margin: 0;
    width: 1200px;
    height: 900px;
    overflow: hidden;
    background: var(--page);
  }
  p, h1 { margin: 0; }
  .billboard {
    position: absolute;
    left: 20px;
    top: 130px;
    width: 1160px;
    height: 640px;
    background: var(--mustard);
    overflow: hidden;
  }
  .billboard__art {
    position: absolute;
    inset: 0;
    width: 1160px;
    height: 640px;
  }
  .brand-name {
    position: absolute;
    left: 0;
    width: 510px;
    top: 148px;
    text-align: center;
    font: 500 26px/1 "Alegreya Sans", sans-serif;
    color: var(--ink);
  }
  .headline {
    position: absolute;
    left: 0;
    width: 510px;
    top: 190px;
    text-align: center;
    font-family: "Alegreya Sans", sans-serif;
  }
  .headline__lead {
    display: block;
    font-weight: 500;
    font-size: 58px;
    line-height: 1;
    color: var(--ink);
  }
  .headline__main {
    display: block;
    font-weight: 800;
    font-size: 96px;
    line-height: 0.95;
    color: var(--crimson);
  }
  .headline__tail {
    display: block;
    font-weight: 500;
    font-size: 70px;
    line-height: 1;
    color: var(--ink);
  }
  .headline-rule {
    position: absolute;
    left: 213px;
    top: 422px;
    width: 84px;
    height: 4px;
    background: var(--crimson);
  }
  .address {
    position: absolute;
    left: 45px;
    top: 450px;
    display: flex;
    align-items: center;
    gap: 12px;
    font: 500 29px/1 "Montserrat", sans-serif;
    color: var(--ink);
    white-space: nowrap;
  }
  .phone {
    position: absolute;
    left: 42px;
    top: 496px;
    font: 500 92px/1 "Roboto Condensed", sans-serif;
    color: var(--white);
    letter-spacing: -1px;
    white-space: nowrap;
  }
  .direction {
    position: absolute;
    left: 597px;
    top: 542px;
    font: 500 44px/1 "Oswald", sans-serif;
    color: var(--crimson);
    white-space: nowrap;
    letter-spacing: -1px;
  }
</style>
</head>
<body>
  <main class="billboard">
    <svg class="billboard__art" viewBox="0 0 1160 640">
      <defs>
        <radialGradient id="ember" cx="0.45" cy="0.4" r="0.7">
          <stop offset="0" stop-color="var(--ember-hot)"/>
          <stop offset="0.45" stop-color="var(--ember-mid)"/>
          <stop offset="1" stop-color="var(--ember-dark)"/>
        </radialGradient>
      </defs>
      <path class="food-photo" role="img" aria-label="Photo of a flaming wok tossing shrimp, broccoli and vegetables"
            d="M500,0 H1160 V640 H820 C690,490 530,300 500,0 Z" fill="url(#ember)"/>
      <path class="swoosh swoosh--black" d="M480,300 C560,420 680,530 860,640 H800 C650,540 530,430 470,320 Z" fill="var(--ink)"/>
      <path class="swoosh swoosh--white" d="M470,200 C520,360 660,520 860,640 H900 C700,510 570,360 520,210 Z" fill="var(--white)"/>
      <path class="direction-banner" d="M575,525 H1060 L1120,565 L1060,605 H575 Z" fill="var(--white)"/>
      <g class="chevrons" fill="none" stroke="var(--ink)" stroke-width="9">
        <path d="M1000,537 L1033,565 L1000,593"/>
        <path d="M1020,537 L1053,565 L1020,593"/>
        <path d="M1040,537 L1073,565 L1040,593"/>
      </g>
    </svg>

    <p class="brand-name">Lotus Leaf Kitchen</p>

    <h1 class="headline">
      <span class="headline__lead">Authentic</span>
      <span class="headline__main">Thai Food</span>
      <span class="headline__tail">Bangkok Style</span>
    </h1>
    <div class="headline-rule"></div>

    <p class="address">
      <svg class="address__pin" width="24" height="34" viewBox="0 0 24 34" aria-hidden="true">
        <path d="M12,0 C5,0 0,5 0,12 C0,21 12,34 12,34 C12,34 24,21 24,12 C24,5 19,0 12,0 Z" fill="var(--crimson)"/>
        <circle cx="12" cy="12" r="4.5" fill="var(--mustard)"/>
      </svg>
      4126 Maple Ridge Rd Otto NC
    </p>

    <p class="phone">828-555-4172</p>

    <p class="direction">6.5 MILES ON THE RIGHT</p>
  </main>
</body>
</html>
```